Leihauto Sperling

We need a web(graphic) design for an landing page on our internet portal providing a search engine to select a rental car. The search engine is using more as 150 rental car providers to find the best price. A comprehensive filter make the selection very quick and effective.
The design should be modern and clean. E.g. this website is what we have seen looks in our opinion good: http://cars.brumbelkart.com

Reason: The decision takes a bit longer

Please change size to 960 px by 1500 px. Also please provide how many photoshop layers your design includes. Thank you.

Rental Car

```html
<!DOCTYPE html>
<html lang="en">
<head>
<meta charset="utf-8">
<title>Leihauto Sperling – Car Rental Comparison</title>
<link href="https://fonts.googleapis.com/css2?family=Roboto+Slab:wght@400;700&family=Lato:wght@400;700;900&display=swap" rel="stylesheet">
<style>
  :root {
    --brand-green: #22c55e;
    --ink: #222222;
    --ink-soft: #333333;
    --white: #ffffff;
    --band-grey: #eceff0;
    --card-yellow: #f0c20f;
    --field-teal: #1abc9c;
    --select-navy: #34495e;
    --cta-red: #f2100c;
    --footer-bg: #232323;
    --footer-text: #f2f2f2;
    --partner-ink: #3a3a3a;
  }
  * { box-sizing: border-box; margin: 0; padding: 0; }
  html, body { width: 800px; height: 1200px; overflow: hidden; background: var(--white); }
  body { position: relative; font-family: 'Lato', sans-serif; color: var(--ink); }

  .site-header { position: absolute; left: 0; top: 0; width: 800px; height: 43px; background: var(--white); }
  .brand { position: absolute; left: 88px; top: 9px; font-family: 'Roboto Slab', serif; font-size: 17px; color: var(--brand-green); border-bottom: 3px solid var(--brand-green); line-height: 20px; padding-bottom: 1px; }
  .main-nav { position: absolute; right: 85px; top: 13px; display: flex; gap: 14px; font-family: 'Roboto Slab', serif; font-size: 13px; color: var(--ink); }
  .main-nav .dot { font-weight: 700; }

  .hero { position: absolute; left: 0; top: 43px; width: 800px; height: 165px; background: linear-gradient(160deg, #5d5d61 0%, #3d3d42 40%, #707074 70%, #4a4a4f 100%); }
  .hero-title { position: absolute; left: 0; width: 800px; top: 52px; text-align: center; font-family: 'Roboto Slab', serif; font-weight: 700; font-size: 31px; color: var(--white); letter-spacing: 0.3px; }
  .btn { position: absolute; background: var(--cta-red); color: var(--white); font-family: 'Roboto Slab', serif; font-size: 10px; text-transform: uppercase; text-align: center; box-shadow: 1px 2px 3px rgba(0,0,0,.35); border-radius: 2px; }
  .hero .btn { left: 354px; top: 101px; width: 94px; height: 26px; line-height: 26px; }

  .partners { position: absolute; left: 0; top: 208px; width: 800px; height: 67px; border-bottom: 1px solid #e6e6e6; }
  .partner { position: absolute; top: 27px; font-family: 'Lato', sans-serif; font-weight: 900; font-size: 14px; color: var(--partner-ink); }

  .band { position: absolute; left: 0; width: 800px; background: var(--band-grey); }
  .band-one { top: 326px; height: 183px; }
  .band-two { top: 641px; height: 181px; }
  .step-number { position: absolute; left: 130px; width: 120px; height: 88px; border-radius: 44px 0 0 44px; background: var(--white); font-family: 'Lato', sans-serif; font-weight: 900; font-size: 46px; padding-left: 20px; line-height: 88px; }
  .step-one { top: 374px; }
  .step-two { top: 689px; }

  .card { position: absolute; left: 235px; width: 333px; background: var(--card-yellow); }
  .card-where { top: 305px; height: 241px; }
  .card-when { top: 582px; height: 296px; }
  .card-badge { position: absolute; left: 60px; top: 17px; width: 183px; height: 56px; }
  .card-badge .label { position: absolute; left: 0; right: 0; top: 12px; text-align: center; font-family: 'Roboto Slab', serif; font-weight: 700; font-size: 19px; color: var(--ink); }

  .field-label { position: absolute; font-size: 12px; color: var(--ink-soft); }
  .field { position: absolute; height: 27px; background: var(--white); border: 2px solid var(--field-teal); border-radius: 3px; font-size: 10px; line-height: 23px; padding-left: 7px; color: var(--ink); }
  .field.placeholder { color: #888; }
  .select-dark .toggle { position: absolute; right: -2px; top: -2px; width: 27px; height: 27px; background: var(--select-navy); border-radius: 0 3px 3px 0; }
  .toggle::after, .select-light::after { content: ""; position: absolute; border-left: 4px solid transparent; border-right: 4px solid transparent; }
  .toggle::after { left: 9px; top: 11px; border-top: 5px solid var(--white); }
  .select-light::after { right: 9px; top: 10px; border-top: 5px solid var(--ink); }
  .date .cal { position: absolute; right: -2px; top: -2px; width: 27px; height: 27px; background: var(--select-navy); border-radius: 0 3px 3px 0; }
  .date .cal::after { content: ""; position: absolute; left: 8px; top: 8px; width: 10px; height: 10px; background: var(--white); border-top: 3px solid #e74c3c; }

  .checkbox { position: absolute; left: 87px; top: 194px; width: 13px; height: 13px; background: var(--field-teal); border-radius: 2px; }
  .checkbox::after { content: ""; position: absolute; left: 4px; top: 1px; width: 4px; height: 8px; border: solid var(--white); border-width: 0 2px 2px 0; transform: rotate(45deg); }

  .card-when .btn { left: 120px; top: 251px; width: 94px; height: 26px; line-height: 26px; }

  .site-footer { position: absolute; left: 0; top: 910px; width: 800px; height: 260px; background: var(--footer-bg); color: var(--footer-text); font-family: 'Roboto Slab', serif; }
  .footer-col { position: absolute; top: 30px; }
  .footer-col h3 { font-size: 12px; font-weight: 700; margin-bottom: 3px; }
  .footer-col li { list-style: none; font-size: 9.5px; line-height: 16px; text-transform: uppercase; }
  .footer-col .gap { margin-top: 16px; }
  .footer-col h3.gap { margin-top: 30px; }
  .legal { position: absolute; left: 90px; top: 1178px; font-family: 'Roboto Slab', serif; font-size: 10px; color: var(--ink); }
</style>
</head>
<body>
  <header class="site-header">
    <div class="brand">Leihauto Sperling</div>
    <nav class="main-nav">
      <span>Rentlane FAQs</span><span class="dot">•</span><span>Help</span><span class="dot">•</span><span>My Booking</span>
    </nav>
  </header>

  <section class="hero" role="img" aria-label="Photo of a silver car in front of a city skyline at night">
    <h1 class="hero-title">WE COMPARE CAR RENTALS</h1>
    <div class="btn">Compare now</div>
  </section>

  <section class="partners" aria-label="Rental partners">
    <span class="partner" style="left:98px">Tallis</span>
    <span class="partner" style="left:180px">Morrow</span>
    <span class="partner" style="left:270px">Vanta</span>
    <span class="partner" style="left:347px">Kestrel</span>
    <span class="partner" style="left:439px">Thrifton</span>
    <span class="partner" style="left:533px">Saverly</span>
    <span class="partner" style="left:639px">Meridia</span>
  </section>

  <div class="band band-one"></div>
  <div class="step-number step-one">#1</div>
  <form class="card card-where">
    <div class="card-badge">
      <svg width="183" height="56" viewBox="0 0 183 56"><polygon points="0,4 178,0 183,38 120,56 40,48" fill="#fff"/><path d="M62 44 Q90 36 122 40" stroke="#222" stroke-width="3" fill="none"/></svg>
      <div class="label">Where?</div>
    </div>
    <span class="field-label" style="left:48px;top:106px">Country:</span>
    <div class="field select-dark" style="left:127px;top:101px;width:156px">Australia<span class="toggle"></span></div>
    <span class="field-label" style="left:54px;top:150px">Pickup:</span>
    <div class="field placeholder" style="left:127px;top:145px;width:156px">City or airport code</div>
    <span class="checkbox"></span>
    <span class="field-label" style="left:107px;top:193px">Return to the same location</span>
  </form>

  <div class="band band-two"></div>
  <div class="step-number step-two">#2</div>
  <form class="card card-when">
    <div class="card-badge">
      <svg width="183" height="56" viewBox="0 0 183 56"><polygon points="0,4 178,0 183,38 120,56 40,48" fill="#fff"/><path d="M66 44 Q92 36 118 40" stroke="#222" stroke-width="3" fill="none"/></svg>
      <div class="label">When?</div>
    </div>
    <span class="field-label" style="left:22px;top:106px">Pickup on:</span>
    <div class="field date" style="left:87px;top:99px;width:104px">05-Aug-2014<span class="cal"></span></div>
    <span class="field-label" style="left:209px;top:106px">at:</span>
    <div class="field select-light" style="left:229px;top:99px;width:75px">10:00 AM</div>

    <span class="field-label" style="left:22px;top:142px">Return on:</span>
    <div class="field date" style="left:87px;top:135px;width:104px">05-Aug-2014<span class="cal"></span></div>
    <span class="field-label" style="left:209px;top:142px">at:</span>
    <div class="field select-light" style="left:229px;top:135px;width:75px">10:00 AM</div>

    <span class="field-label" style="left:22px;top:177px">I live in:</span>
    <div class="field select-light" style="left:87px;top:170px;width:184px">Australia</div>

    <span class="field-label" style="left:22px;top:212px">Driver age</span>
    <div class="field select-light" style="left:87px;top:205px;width:73px">10:00 AM</div>

    <div class="btn">Search</div>
  </form>

  <footer class="site-footer">
    <div class="footer-col" style="left:128px">
      <h3>EXTRA STUFF</h3>
      <ul>
        <li>Site map</li><li>Campervans</li><li>Price promise</li><li>Blog</li><li>Newsletter</li><li>Meet the Brumbel team</li><li>Happy customers</li><li>Why us?</li>
        <li class="gap">Chirpline</li><li>Friendbook</li><li>Blog</li>
      </ul>
    </div>
    <div class="footer-col" style="left:344px">
      <h3>MORE COUNTRIES</h3>
      <ul>
        <li>Scotland</li><li>Northern Ireland</li><li>Germany</li><li>Spain</li><li>France</li><li>Italy</li><li>Croatia</li>
      </ul>
    </div>
    <div class="footer-col" style="left:564px">
      <h3>LEAVING EUROPE</h3>
      <ul>
        <li>USA car rental</li><li>Canada car rental</li><li>Australia car rental</li><li>New Zealand car rental</li><li>Fiji car rental</li>
      </ul>
      <h3 class="gap">FUN GUIDES &amp; TIPS</h3>
      <ul>
        <li>Our content articles</li><li>Location guides</li>
      </ul>
    </div>
  </footer>
  <p class="legal">© Leihauto Sperling 2014. All Rights Reserved</p>
</body>
</html>
```